Site for company producing and selling products for children's health

We need an appealing professional web site design and images for a brand new company producing and selling products focused on children’s health. The site will offer information to visitors on the company, the company’s products, and general resources related to children’s health. Additionally the site will offer e-commerce functionality to allow for ordering of the company’s products.
The content and navigation for the site will be generated by programming, such as php or asp, and therefore any images used in the navigation portions of the site should allow for HTML markup to be overlaid rather than having the text built into the image or graphic.
The design must include 2 layouts, one for the landing/home page that includes only top navigation, and an inner page layout that includes both top and left navigation.
The header area of the site should include a place for links to access the visitor’s cart and profile similar to the top sections of plumvat.com, tidelor.com, and keenmart.com.
The landing page of the site should include some type of “changing” image area where we can include multiple image files for rotation to visitors similar to what is seen at vorta.com or brisksip.com. The flash/animation mechanism does not need to be provided (although it would be a plus if it was) but the design must accommodate the space for it.
The company’s colors are Orange (FF9900) and Blue (0066FF) and the logo can be viewed at http://wonkibrook.com/logo.png
All CSS and markup provided must be display consistently in Internet Explorer 7+, FifeFox, Google Chrome, and Safari.
Incorporating social media links (facebook, twitter, etc.) is desirable.
Parents who are conscious of health risks associated with children's diets and consumer food products.
E-Commerce

```html
<!DOCTYPE html>
<html lang="en">
<head>
<meta charset="utf-8">
<title>Wonki Brook – Healthy Products for Growing Children</title>
<link href="https://fonts.googleapis.com/css2?family=Open+Sans:wght@400;600;700&display=swap" rel="stylesheet">
<style>
:root{
  --orange:#ff9900;
  --orange-light:#ffb43a;
  --orange-dark:#f08400;
  --blue:#0066ff;
  --blue-light:#3d8cff;
  --blue-dark:#0050d8;
  --ink:#1b1b1b;
  --muted:#666;
  --grey-panel:#ececec;
  --grey-line:#d6d6d6;
  --footer-top:#cfe0fb;
  --footer-bottom:#8fb4f2;
  --white:#fff;
}
*{box-sizing:border-box;margin:0;padding:0}
html,body{width:783px;height:1200px;overflow:hidden}
body{position:relative;background:var(--white);font-family:"Open Sans",Verdana,sans-serif;color:var(--ink);font-size:11px}
a{color:inherit;text-decoration:none}
.abs{position:absolute}

/* header */
.brand{left:22px;top:22px;display:flex;align-items:center;gap:10px}
.brand-dot{width:40px;height:40px;border-radius:50%;background:var(--blue)}
.brand-name{font-size:32px;font-weight:700;color:var(--orange);letter-spacing:-.5px}
.welcome-note{right:23px;top:20px;color:var(--orange);font-size:12px}
.account-links{right:23px;top:38px;font-size:10.5px;color:#333}
.search{right:27px;top:63px;display:flex;gap:5px}
.search-field{width:140px;height:16px;background:#f1f1f1;border:1px solid #e2e2e2;font-size:9.5px;color:#999;padding:1px 5px}
.search-btn{width:41px;height:16px;background:var(--blue);color:var(--white);font-size:10px;text-align:center;line-height:16px}

.main-nav{left:23px;top:99px;width:737px;height:32px;border-radius:5px;background:linear-gradient(var(--orange-light),var(--orange-dark));display:flex}
.main-nav a{flex:1;color:var(--white);font-size:13px;text-align:center;line-height:32px;border-right:1px solid #ffc56a}
.main-nav a:last-child{border-right:none}

/* sidebar */
.side-box{left:23px;width:150px;border-radius:4px;padding:10px 10px}
.box-blue{background:linear-gradient(var(--blue-light),var(--blue));color:var(--white)}
.box-orange{background:linear-gradient(var(--orange-light),var(--orange-dark));color:var(--white)}
.box-grey{background:var(--grey-panel);border:1px solid var(--grey-line)}
.side-title{font-size:13px;margin-bottom:4px}
.side-text{font-size:10.5px;line-height:1.25}
.cart{top:153px;height:83px}
.cart-count{margin-top:7px;font-size:12px}
.cart-icon{right:10px;bottom:12px}
.compare{top:256px;height:82px}
.newsletter{top:356px;height:110px}
.newsletter input{display:block;width:130px;height:16px;border:none;margin:9px 0 6px}
.subscribe-btn{display:inline-block;background:#111;color:var(--white);font-weight:700;font-size:10.5px;padding:2px 9px;border-radius:4px}
.category{top:487px;height:273px;background:var(--grey-panel);border-radius:4px;padding:10px 0 0}
.category h3{font-weight:400;font-size:14px;color:var(--orange);padding:0 10px;margin-bottom:4px}
.category li{list-style:none;font-size:10.5px;margin:0 10px;height:23.6px;line-height:23.6px;border-bottom:1px dotted #bbb}
.delivery{top:780px;height:94px}
.delivery .big{font-size:26px;font-weight:700;left:34px;top:38px}
.guarantee{top:894px;height:93px}
.guarantee-seal{right:8px;top:36px;width:50px;height:50px;border-radius:50%;background:#e9f1ff;border:3px solid #bcd4ff}

/* banner */
.banner{left:193px;top:155px;width:567px;height:311px;border:3px solid var(--orange);border-radius:4px;background:linear-gradient(90deg,#fff 0%,#fff 45%,#ffe3b8 100%);overflow:hidden}
.banner-photo{position:absolute;left:20px;top:20px;width:340px;height:260px;border-radius:6px;background:radial-gradient(ellipse at 50% 55%,#f3c16a 0%,#e8a84d 30%,#fdf4e6 70%,#fff 100%)}
.banner-copy{position:absolute;left:370px;top:25px;width:185px}
.banner-copy h2{font-size:26px;font-weight:600;color:var(--orange);line-height:1.1}
.banner-copy h3{font-size:14px;font-weight:700;line-height:1.2;margin-bottom:14px}
.banner-copy p{font-size:10.5px;line-height:1.3}
.read-more{display:inline-block;margin-top:8px;background:var(--blue);color:var(--white);font-weight:700;font-size:10.5px;padding:3px 8px;border-radius:4px}
.thumbs{position:absolute;right:10px;bottom:10px;display:flex;gap:9px}
.thumb{width:55px;height:55px;border:2px solid #7aa8ff;border-radius:4px;background:linear-gradient(#e8f1ff,#bcd6ff)}

/* intro */
.intro-title{left:193px;top:484px;font-size:20px;font-weight:400}
.intro-title span{color:var(--orange)}
.intro-photo{left:582px;top:518px;width:174px;height:109px;border-radius:6px;background:linear-gradient(135deg,#e8d2bd,#c79b76 60%,#8aa0c8)}
.intro-copy{left:193px;top:516px;width:570px;font-size:10.5px;line-height:1.3}
.intro-copy p{margin-bottom:12px}
.narrow{width:380px}

/* products */
.products-title{left:193px;top:696px;font-size:15px}
.card{top:726px;width:183px;height:244px;background:var(--grey-panel);border-radius:3px}
.card-photo{position:absolute;left:17px;top:15px;width:149px;height:147px;background:var(--white);border:1px solid #d4d4d4;padding:8px}
.card-photo i{display:block;width:100%;height:100%;border-radius:4px}
.card-name{position:absolute;left:17px;top:178px;font-size:11px;font-weight:700;line-height:1.2}
.card-actions{position:absolute;left:17px;top:215px;display:flex;gap:4px}
.btn-cart,.btn-details{font-size:9.5px;color:var(--white);padding:2px 0;width:75px;text-align:center;border-radius:3px 0 0 3px}
.btn-cart{background:var(--orange)}
.btn-details{background:var(--blue-light);width:56px;border-radius:0 3px 3px 0}
.pager{left:652px;top:982px;display:flex;align-items:center;gap:6px;font-size:11px;font-weight:700}

/* footer */
.footer{left:0;top:1025px;width:783px;height:153px;background:linear-gradient(var(--footer-top),var(--footer-bottom))}
.foot-col{top:18px;width:150px;padding-left:0;border-right:1px solid #b4cdf3;height:118px}
.foot-col h4{color:var(--blue);font-size:11px;font-weight:700;margin-bottom:8px}
.foot-col li{list-style:none;color:var(--blue);font-size:9.5px;line-height:19px}
.trust{left:520px;top:27px;width:240px;height:108px;background:var(--white);border-radius:5px;display:grid;grid-template-columns:repeat(3,1fr);gap:10px;padding:14px 16px;align-items:center;justify-items:center}
.trust span{display:block;width:52px;height:30px;border-radius:4px;background:#dfe6f0}
.trust span.round{width:34px;height:34px;border-radius:50%}
.bottom-bar{left:0;top:1178px;width:783px;height:22px;background:linear-gradient(var(--orange-light),var(--orange-dark));font-size:9.5px;line-height:22px;padding:0 23px;display:flex;justify-content:space-between}
.social{display:flex;align-items:center;gap:6px}
.social i{width:15px;height:15px;border-radius:50%;background:var(--white);opacity:.9}
</style>
</head>
<body>

<header>
  <a class="brand abs" href="#"><span class="brand-dot"></span><span class="brand-name">wonkibrook</span></a>
  <div class="welcome-note abs">Welcome to our online store!</div>
  <div class="account-links abs">My Account - My Wishlist - My Cart - Checkout - Login</div>
  <form class="search abs"><div class="search-field">Search Entire Store Now....</div><div class="search-btn">Search</div></form>
  <nav class="main-nav abs">
    <a href="#">Home</a><a href="#">About Us</a><a href="#">Products</a><a href="#">Services</a><a href="#">News</a><a href="#">Contact Us</a>
  </nav>
</header>

<aside>
  <div class="side-box box-blue cart abs">
    <div class="side-title">My Cart</div>
    <div class="side-text">You have no items in<br>your shopping cart.</div>
    <div class="cart-count">0 Item &nbsp;| &nbsp;0 $</div>
    <svg class="cart-icon abs" width="40" height="32" viewBox="0 0 40 32" fill="none" stroke="#fff" stroke-width="2.2"><path d="M2 4h6l5 17h20l4-12H11"/><circle cx="15" cy="27" r="2.5"/><circle cx="30" cy="27" r="2.5"/></svg>
  </div>
  <div class="side-box box-grey compare abs">
    <div class="side-title">Compare Products</div>
    <div class="side-text">You have no products<br>to compare.</div>
  </div>
  <div class="side-box box-orange newsletter abs">
    <div class="side-title">Newsletter Signup</div>
    <div class="side-text">Signup for our Newsletter:</div>
    <input type="text" aria-label="Email">
    <span class="subscribe-btn">Subscribe</span>
  </div>
  <div class="side-box category abs">
    <h3>Product Category</h3>
    <ul>
      <li>Product Category 1</li><li>Product Category 2</li><li>Product Category 4</li><li>Product Category 4</li><li>Product Category 5</li><li>Product Category 6</li><li>Product Category 7</li><li>Product Category 8</li><li>Product Category 9</li><li>Product Category 10</li>
    </ul>
  </div>
  <div class="side-box box-orange delivery abs">
    <div class="side-title" style="font-size:15px">Fast Delivery</div>
    <div class="side-text" style="margin-top:6px">within</div>
    <div class="big abs">3</div>
    <div class="side-text abs" style="left:43px;top:72px">Days</div>
    <svg class="abs" style="right:10px;top:38px" width="62" height="42" viewBox="0 0 62 42"><rect x="2" y="6" width="36" height="24" fill="#e07000"/><path d="M38 14h12l8 9v7H38z" fill="#e07000"/><circle cx="14" cy="33" r="5" fill="#6b3a00"/><circle cx="48" cy="33" r="5" fill="#6b3a00"/></svg>
  </div>
  <div class="side-box box-blue guarantee abs">
    <div class="side-title" style="font-size:14px">100% Money Back</div>
    <div class="side-title" style="font-weight:700">Guarantee</div>
    <div class="guarantee-seal abs"></div>
  </div>
</aside>

<main>
  <section class="banner abs">
    <div class="banner-photo" role="img" aria-label="Group of happy children jumping in the air"></div>
    <div class="banner-copy">
      <h2>Wonki Brook</h2>
      <h3>brings Healthy Products<br>for your Growing Child</h3>
      <p>Lorem Ipsum is simply dummy text of the printing and typesetting industry. Lorem Ipsum has been the industry's standard dummy text ever since the 1500s.</p>
      <a class="read-more" href="#">Read More</a>
    </div>
    <div class="thumbs">
      <div class="thumb" role="img" aria-label="Baby in bath"></div>
      <div class="thumb" role="img" aria-label="Baby lotion bottle"></div>
      <div class="thumb" role="img" aria-label="Baby toy"></div>
    </div>
  </section>

  <h1 class="intro-title abs">Welcome to <span>Wonki Brook</span></h1>
  <div class="intro-photo abs" role="img" aria-label="Smiling family of parents and children together"></div>
  <div class="intro-copy abs">
    <p class="narrow">Lorem Ipsum is simply dummy text of the printing and typesetting industry. Lorem Ipsum has been the industry's standard dummy text ever since the 1500s, when an unknown printer took a galley of type and scrambled it to make a type specimen book.</p>
    <p class="narrow">It has survived not only five centuries, but also the leap into electronic typesetting, remaining essentially unchanged. It was popularised in the 1960s with the release of Lettrane sheets containing Lorem PageSetter including versions of Lorem Ipsum</p>
    <p>Contrary to popular belief, Lorem Ipsum is not simply random text. It has roots in a piece of classical Latin literature from 45 BC, making it over 2000 years old. Rupert Marlowe, a Latin professor at Hollin-Vale College in Vermont, looked up one of the more obscure Latin words, consectetur, from a Lorem Ipsum passage, and going through the cites of the word in classical literature, discovered the undoubtable source.</p>
  </div>

  <h2 class="products-title abs">Products</h2>
  <article class="card abs" style="left:193px">
    <div class="card-photo"><i role="img" aria-label="Set of baby care bottles and cream" style="background:linear-gradient(#f4e7f2,#fdf2c4 50%,#fbd2d8)"></i></div>
    <div class="card-name">Lorem Ipsum is<br>simply dummy text</div>
    <div class="card-actions"><span class="btn-cart">Add to Cart</span><span class="btn-details">Details</span></div>
  </article>
  <article class="card abs" style="left:384px">
    <div class="card-photo"><i role="img" aria-label="Baby clothing set with hooded towel" style="background:linear-gradient(135deg,#eef2fb,#dfe4f3 50%,#f2d9c4)"></i></div>
    <div class="card-name">Lorem Ipsum is<br>simply dummy text</div>
    <div class="card-actions"><span class="btn-cart">Add to Cart</span><span class="btn-details">Details</span></div>
  </article>
  <article class="card abs" style="left:575px">
    <div class="card-photo"><i role="img" aria-label="Range of children's skin care bottles" style="background:linear-gradient(#f3f8ee,#dff0d0 60%,#f7f7f7)"></i></div>
    <div class="card-name">Lorem Ipsum is<br>simply dummy text</div>
    <div class="card-actions"><span class="btn-cart">Add to Cart</span><span class="btn-details">Details</span></div>
  </article>

  <div class="pager abs">
    <svg width="12" height="12" viewBox="0 0 12 12"><path d="M8 1 3 6l5 5" stroke="#ff9900" stroke-width="2.5" fill="none"/></svg>
    <span>1 | 2 | 3 | 4..</span>
    <svg width="12" height="12" viewBox="0 0 12 12"><path d="M4 1l5 5-5 5" stroke="#ff9900" stroke-width="2.5" fill="none"/></svg>
  </div>
</main>

<footer>
  <div class="footer abs">
    <div class="foot-col abs" style="left:24px"><h4>Products</h4><ul><li>Product Category 1</li><li>Product Category 2</li><li>Product Category 3</li><li>Product Category 4</li><li>Product Category 5</li></ul></div>
    <div class="foot-col abs" style="left:175px"><h4>Services</h4><ul><li>Service Category 1</li><li>Service Category 2</li><li>Service Category 3</li><li>Service Category 4</li><li>Service Category 5</li></ul></div>
    <div class="foot-col abs" style="left:318px;border:none"><h4>News</h4><ul><li>New Archieve 1</li><li>New Archieve 2</li><li>New Archieve 3</li><li>New Archieve 4</li><li>New Archieve 5</li></ul></div>
    <div class="trust abs">
      <span class="round"></span><span class="round"></span><span></span>
      <span></span><span class="round"></span><span></span>
    </div>
  </div>
  <div class="bottom-bar abs">
    <span>Copyright © 2010 Wonki Brook. All Rights Reserved | Legal | Privacy Policy</span>
    <span class="social">Connect With Us : <i></i><i></i><i></i><i></i></span>
  </div>
</footer>

</body>
</html>
```